Willow Crossing: A Self Care Session for Employees

I need a flyer for organizations and businnesses. I am offering a session that will address behavioral issues such as coming to work late, not getting along with others and not working together as a team. I am a life coach who works with difficult employees, helping them address their issues and helping them be a better version of themselves. I also offer a leadership class for managers. I would like the flyer to be professional, clean and convey a feeling of trust. I would prefer to see disgns that use the color blue.

Target Market(s)

small businesses

Industry/Entity Type

Work

Font styles to use
Sans Serif

Colors
34a7d8
85cae6
0792cd
ffffff

Requirements
Must have
• shades of blue and perhaps white. should be clean, fresh and professional
Nice to have
• simple yet warm
Should not have
• distracting and heavy, playful

```html
<!DOCTYPE html>
<html lang="en">
<head>
<meta charset="utf-8">
<title>Willow Crossing: A Self Care Session for Employees</title>
<link rel="stylesheet" href="https://fonts.googleapis.com/css2?family=Roboto:wght@300;400;700;900&family=Roboto+Condensed:wght@300;400;700&display=swap">
<style>
  :root {
    --blue-deep: #2e3a9e;
    --blue-mid: #1f5fc0;
    --blue-bright: #0792cd;
    --blue-sky: #34a7d8;
    --blue-pale: #85cae6;
    --teal-name: #7fd3d6;
    --white: #ffffff;
    --ink: #111111;
    --bar-dark: #333333;
    --bar-mid: #4a4a4a;
    --bar-light: #6b6b6b;
  }
  html, body {
    margin: 0;
    padding: 0;
    overflow: hidden;
    background: var(--white);
  }
  .flyer {
    position: relative;
    width: 927px;
    height: 1200px;
    overflow: hidden;
    background: var(--white);
    font-family: "Roboto", Arial, sans-serif;
  }
  .title-panel {
    position: absolute;
    left: 122px;
    top: 0;
    width: 427px;
    height: 740px;
    background:
      linear-gradient(115deg, rgba(7,146,205,0.55) 0%, rgba(7,146,205,0) 40%),
      linear-gradient(200deg, rgba(52,167,216,0.7) 0%, rgba(52,167,216,0) 45%),
      linear-gradient(180deg, var(--blue-mid) 0%, var(--blue-deep) 55%, #4356b0 100%);
  }
  .panel-fade {
    position: absolute;
    left: 122px;
    top: 740px;
    width: 427px;
    height: 180px;
    background: linear-gradient(180deg, #c7cdea 0%, rgba(255,255,255,0) 100%);
  }
  .photo-area {
    position: absolute;
    left: 549px;
    top: 170px;
    width: 378px;
    height: 570px;
    background: linear-gradient(160deg, #eef1f4 0%, #cfd6df 40%, #2d4a56 75%, #1e3038 100%);
  }
  .headline {
    position: absolute;
    left: 146px;
    top: 0;
    margin: 0;
    color: var(--white);
  }
  .headline span {
    position: absolute;
    left: 0;
    white-space: nowrap;
    line-height: 1;
  }
  .hl-light { font-weight: 300; }
  .hl-bold { font-weight: 900; letter-spacing: -1px; }
  .hl-a { top: 228px; font-size: 60px; }
  .hl-self { top: 290px; font-size: 82px; }
  .hl-care { top: 370px; font-size: 82px; }
  .hl-session { top: 456px; font-size: 64px; }
  .hl-for { top: 523px; font-size: 64px; }
  .hl-employees { top: 586px; font-size: 62px; }
  .coach-name {
    position: absolute;
    left: 146px;
    top: 660px;
    margin: 0;
    font-weight: 300;
    font-size: 57px;
    line-height: 1;
    color: var(--teal-name);
    white-space: nowrap;
  }
  .questions {
    position: absolute;
    left: 145px;
    top: 770px;
    margin: 0;
    font-family: "Roboto Condensed", "Arial Narrow", sans-serif;
    color: var(--ink);
    font-size: 36px;
    line-height: 1;
  }
  .questions p { margin: 0; white-space: nowrap; }
  .questions .q-light { font-weight: 300; }
  .questions strong { font-weight: 700; }
  .q1 { height: 42px; }
  .q2 { height: 52px; }
  .q3 { height: 42px; }
  .pitch {
    position: absolute;
    left: 148px;
    top: 962px;
    margin: 0;
    font-family: "Roboto Condensed", "Arial Narrow", sans-serif;
    font-weight: 300;
    font-size: 26px;
    line-height: 34px;
    color: var(--ink);
  }
  .footer-bar {
    position: absolute;
    left: 0;
    top: 1058px;
    width: 927px;
    height: 142px;
  }
  .footer-bar svg { position: absolute; left: 0; top: 0; }
  .session-tag {
    position: absolute;
    left: 139px;
    top: 26px;
    margin: 0;
    color: var(--white);
    font-family: "Roboto", Arial, sans-serif;
    font-weight: 400;
    line-height: 1;
  }
  .session-tag .tag-label { display: block; font-size: 20px; margin-bottom: 10px; }
  .session-tag .tag-title { display: block; font-size: 26px; line-height: 30px; }
  .contact {
    position: absolute;
    left: 522px;
    top: 24px;
    margin: 0;
    color: var(--white);
    font-family: "Roboto Condensed", "Arial Narrow", sans-serif;
    font-weight: 400;
    font-size: 22px;
    line-height: 29px;
  }
  .contact strong { font-weight: 700; font-size: 23px; }
</style>
</head>
<body>
<main class="flyer">
  <div class="title-panel"></div>
  <div class="panel-fade"></div>
  <div class="photo-area" role="img" aria-label="Photo of a stressed businessman at a laptop holding his head in his hands"></div>

  <h1 class="headline">
    <span class="hl-a hl-light">A</span>
    <span class="hl-self hl-bold">SELF</span>
    <span class="hl-care hl-bold">CARE</span>
    <span class="hl-session hl-light">SESSION</span>
    <span class="hl-for hl-light">FOR</span>
    <span class="hl-employees hl-bold">EMPLOYEES</span>
  </h1>
  <p class="coach-name">MARISOL KEANE</p>

  <div class="questions">
    <p class="q1 q-light">ARE YOUR EMPLOYEES BRINGING</p>
    <p class="q2"><strong>PERSONAL ISSUES ON THE JOB?</strong></p>
    <p class="q3"><span class="q-light">IS IT AFFECTING TEAM </span><strong>COMMUNICATION</strong></p>
    <p class="q4"><span class="q-light">OR MAY BE EVEN </span><strong>PRODUCTIVITY?</strong></p>
  </div>

  <p class="pitch">If the behavior of an employee,<br>manager or your entire staff is a problem I can help.</p>

  <footer class="footer-bar">
    <svg width="927" height="142" viewBox="0 0 927 142" aria-hidden="true">
      <rect x="0" y="0" width="927" height="142" fill="var(--bar-light)"/>
      <polygon points="0,0 505,0 565,71 505,142 0,142" fill="var(--bar-mid)"/>
      <polygon points="0,0 440,0 480,71 440,142 0,142" fill="var(--bar-dark)"/>
    </svg>
    <p class="session-tag">
      <span class="tag-label">WILLOW CROSSING:</span>
      <span class="tag-title">A SELF CARE SESSION<br>FOR EMPLOYEES</span>
    </p>
    <p class="contact">For more information contact<br>Marisol Keane on<br><strong>555-014-2387 or 555-0193</strong></p>
  </footer>
</main>
</body>
</html>
```